Tovesca Website

I need a website for a startup company that provides GIS (Geographic Information Services) staffing and products for local cities. Current website is www.tovescagroup.com

```html
<!DOCTYPE html>
<html lang="en">
<head>
<meta charset="utf-8">
<title>Tovesca Group</title>
<link href="https://fonts.googleapis.com/css2?family=League+Spartan:wght@300;400;500;600;700&display=swap" rel="stylesheet">
<style>
:root{
  --yellow:#f5c518;
  --ink:#1c1c1c;
  --dark:#242424;
  --card:#dddce5;
  --field:#dddce6;
  --line:#9a9a9a;
  --footer:#3b3b3d;
  --white:#ffffff;
  --muted:#cfcfcf;
}
*{margin:0;padding:0;box-sizing:border-box}
html,body{width:1200px;height:4608px;overflow:hidden}
body{font-family:"League Spartan",sans-serif;color:var(--ink);background:var(--white);position:relative}
.abs{position:absolute}
/* hero */
.hero{position:absolute;left:0;top:0;width:1200px;height:706px;
  background:radial-gradient(ellipse at 70% 35%,#a9650f 0%,#5a300c 35%,#24140a 70%),#1d120a;}
.hero-glow{position:absolute;inset:0;background:radial-gradient(ellipse at 10% 90%,rgba(230,110,20,.55),transparent 45%),radial-gradient(ellipse at 85% 80%,rgba(200,110,20,.35),transparent 40%)}
.nav{position:absolute;left:59px;top:18px;width:1076px;height:75px;border-radius:38px;background:rgba(60,40,20,.55);display:flex;align-items:center;padding:0 32px}
.brand{display:flex;align-items:center;gap:10px;color:var(--white);font-size:19px;font-weight:500;line-height:1}
.brand-dot{width:40px;height:40px;border-radius:50%;background:var(--yellow)}
.nav-links{display:flex;gap:34px;margin-left:150px;color:var(--white);font-size:12px;letter-spacing:.3px}
.btn{display:flex;align-items:center;justify-content:center;background:var(--yellow);color:var(--ink);font-weight:700;font-size:12px;border-radius:30px;box-shadow:0 6px 16px rgba(245,197,24,.45)}
.nav .btn{margin-left:auto;width:104px;height:42px}
.hero-text{position:absolute;left:0;width:1200px;text-align:center;color:var(--white)}
/* about */
.about-title{left:75px;top:820px;font-size:78px;font-weight:500;line-height:84px}
.photo{position:absolute;left:75px;width:492px}
.block{position:absolute;left:635px;width:513px;border-top:1.5px solid var(--line);padding:22px 12px 0 13px}
.block h3{font-size:22px;font-weight:400;margin-bottom:12px}
.block h3 b{font-size:38px;font-weight:500;margin-right:8px}
.block p{font-size:12.5px;line-height:14.5px;margin-bottom:14px}
/* services */
.section-title{position:absolute;left:0;width:1200px;text-align:center;font-size:76px;font-weight:500}
.section-sub{position:absolute;left:0;width:1200px;text-align:center;font-size:13px;line-height:16px}
.card{position:absolute;top:2128px;width:325px;height:400px;border-radius:30px;background:var(--card);padding:32px 34px}
.card.dark{background:var(--dark);color:var(--white)}
.card h4{margin-top:104px;font-size:20px;font-weight:400;padding-bottom:12px;border-bottom:2px solid currentColor;width:200px;white-space:nowrap}
.card ul{margin-top:22px;list-style:none;font-size:13px;line-height:24.5px}
.card li::before{content:"•";margin:0 12px 0 6px}
.card .icon{position:absolute;left:34px;top:18px}
.card .arrow{position:absolute;left:34px;bottom:30px}
/* products */
.products{position:absolute;left:0;top:2652px;width:1200px;height:954px;
  background:linear-gradient(180deg,#1a2230 0%,#3b4350 22%,#6b717c 45%,#2b313b 70%,#0d1014 100%)}
.tabs{position:absolute;left:60px;top:2825px;width:1080px;display:flex;justify-content:space-between;color:var(--white);font-size:14px;text-align:center;line-height:14px}
.tabs span{width:190px}
.tabs .on{font-weight:700;color:var(--white)}
.tabs .off{color:#d6d6d6}
.tile{position:absolute;width:350px;height:340px;background:#2e2e2e;padding:12px;color:var(--white);text-align:center}
.tile.hl{background:#e9c75b;color:var(--ink)}
.tile .pic{width:326px;height:222px}
.tile h5{font-size:20px;font-weight:400;margin-top:12px}
.tile p{font-size:12.5px;line-height:14px;margin:6px 20px 0}
.round{position:absolute;width:32px;height:32px;border-radius:50%;background:var(--white)}
/* contact */
.field{position:absolute;left:293px;width:614px;background:var(--field);border-radius:12px;padding:17px 20px;font-size:13px}
/* footer */
.footer{position:absolute;left:0;top:4338px;width:1200px;height:270px;background:var(--footer);color:var(--white)}
.fcol{position:absolute;font-size:14px;line-height:28px}
.fcol h6{font-size:13px;font-weight:700;letter-spacing:.4px;margin-bottom:6px}
</style>
</head>
<body>

<section class="hero">
  <div class="hero-glow" role="img" aria-label="Glowing orange topographic contour lines over a dark background"></div>
  <nav class="nav">
    <div class="brand"><span class="brand-dot"></span><span>TOVESCA<br>GROUP</span></div>
    <div class="nav-links"><span>HOME</span><span>ABOUT US</span><span>SERVICES</span><span>PRODUCTS</span><span>CONTACT US</span></div>
    <div class="btn">LOGIN</div>
  </nav>
  <p class="hero-text" style="top:248px;font-size:13px">We Make GIS Work For You</p>
  <h1 class="hero-text" style="top:274px;font-size:40px;font-weight:400;line-height:42px">"Transforming Data Into Insights: Your<br>Trusted GIS Partner"</h1>
  <p class="hero-text" style="top:373px;font-size:18px">Empowering Decisions Through Cutting-Edge Geographic Information Services.</p>
  <div class="btn abs" style="left:506px;top:417px;width:186px;height:40px;font-size:11px">GET STARTED TODAY</div>
</section>

<h2 class="abs about-title">About Us |<br>Tovesca<br>Group</h2>
<div class="photo" style="top:1109px;height:225px;background:linear-gradient(135deg,#2a6fb0,#3aa27a 45%,#d9b43a 75%,#c8542a)" role="img" aria-label="Colour-coded aerial elevation map of a city with a stadium"></div>
<div class="photo" style="top:1366px;height:224px;background:linear-gradient(135deg,#4fc4e8,#3ab4dc)" role="img" aria-label="Red paper plane flying towards a red target on a blue background"></div>
<div class="photo" style="top:1622px;height:222px;background:linear-gradient(90deg,#d9bf95,#2c8e8a 45%,#d8bd91 70%,#c9a87a)" role="img" aria-label="Hand placing wooden blocks reading our mission"></div>

<div class="block" style="top:830px">
  <h3><b>1</b>WHO ARE WE?</h3>
  <p>Lorem Ipsum È Un Testo Segnaposto Utilizzato Nel Settore Della Tipografia E Della Stampa</p>
  <p>Lorem Ipsum È Un Testo Segnaposto Utilizzato Nel Settore Della Tipografia E Della Stampa. Lorem Ipsum È Considerato Il Testo Segnaposto Standard Sin Dal Sedicesimo Secolo, Quando Un Anonimo Tipografo Prese Una Cassetta Di Caratteri E Li Assemblò Per Preparare Un Testo Campione. È Sopravvissuto Non Solo A Più Di Cinque Secoli, Ma Anche Al Passaggio Alla Videoimpaginazione, Pervenendoci Sostanzialmente Inalterato.</p>
</div>
<div class="block" style="top:1096px">
  <h3><b>2</b>OUR VISION</h3>
  <p>Lorem Ipsum È Un Testo Segnaposto Utilizzato Nel Settore Della Tipografia E Della Stampa</p>
  <p>Lorem Ipsum È Un Testo Segnaposto Utilizzato Nel Settore Della Tipografia E Della Stampa. Lorem Ipsum È Considerato Il Testo Segnaposto Standard Sin Dal Sedicesimo Secolo, Quando Un Anonimo Tipografo Prese Una Cassetta Di Caratteri E Li Assemblò Per Preparare Un Testo Campione. È Sopravvissuto Non Solo A Più Di Cinque Secoli, Ma Anche Al Passaggio Alla Videoimpaginazione, Pervenendoci Sostanzialmente Inalterato.</p>
</div>
<div class="block" style="top:1379px">
  <h3><b>3</b>OUR MISSION</h3>
  <p style="padding-right:100px">Lorem Ipsum È Un Testo Segnaposto Utilizzato Nel Settore Della Tipografia E Della Stampa</p>
  <p style="padding-right:100px">Lorem Ipsum È Un Testo Segnaposto Utilizzato Nel Settore Della Tipografia E Della Stampa</p>
  <p>Lorem Ipsum È Un Testo Segnaposto Utilizzato Nel Settore Della Tipografia E Della Stampa. Lorem Ipsum È Considerato Il Testo Segnaposto Standard Sin Dal Sedicesimo Secolo, Quando Un Anonimo Tipografo Prese Una Cassetta Di Caratteri E Li Assemblò Per Preparare Un Testo Campione. È Sopravvissuto Non Solo A Più Di Cinque Secoli, Ma Anche Al Passaggio Alla Videoimpaginazione, Pervenendoci Sostanzialmente Inalterato. Lorem Ipsum È Un Testo Segnaposto Utilizzato Nel Settore Della Tipografia E Della Stampa. Lorem Ipsum È Considerato Il Testo Segnaposto Standard Sin Dal Sedicesimo Secolo, Quando Un Anonimo Tipografo Prese Una Cassetta Di Caratteri E Li Assemblò Per Preparare Un Testo Campione. È Sopravvissuto Non Solo A Più Di Cinque Secoli, Ma Anche Al Passaggio Alla Videoimpaginazione, Pervenendoci Sostanzialmente Inalterato.</p>
</div>
<div class="btn abs" style="left:647px;top:1802px;width:286px;height:43px">CLICK HERE FOR MORE INFORMATION</div>

<h2 class="section-title" style="top:1950px">Our Services</h2>
<p class="section-sub" style="top:2062px">Accurate &amp; Precise Land Surveying Services With The<br>Highest Quality.</p>

<div class="card" style="left:63px">
  <svg class="icon" width="96" height="96" viewBox="0 0 96 96" fill="none" stroke="#1c1c1c" stroke-width="3"><circle cx="48" cy="40" r="16"/><circle cx="48" cy="40" r="6"/><path d="M16 86v-10h20v10M60 86v-10h20v10"/><circle cx="26" cy="62" r="6"/><circle cx="70" cy="62" r="6"/></svg>
  <h4>GIS CONSULTING</h4>
  <ul><li>GIS Projects</li><li>Staffing Solutions</li><li>System Architecture Design</li><li>GIS Analysis</li><li>Demographics</li><li>Map Products</li></ul>
  <svg class="arrow" width="44" height="36" viewBox="0 0 44 36" fill="none" stroke="#1c1c1c" stroke-width="5"><path d="M2 18h38M24 3l16 15-16 15"/></svg>
</div>
<div class="card dark" style="left:438px">
  <svg class="icon" width="96" height="96" viewBox="0 0 96 96" fill="none" stroke="#ffffff" stroke-width="3"><rect x="10" y="14" width="76" height="66" rx="4"/><path d="M10 28h76"/><circle cx="52" cy="56" r="14"/><circle cx="52" cy="56" r="5"/></svg>
  <h4>GIS APPLICATIONS</h4>
  <ul><li>MapCloud Online</li><li>MapCloud Enterprise</li><li>Dashboards</li><li>Layout Builder</li><li>Custom Widgets</li><li>Custom JavaScript Apps</li></ul>
  <svg class="arrow" width="44" height="36" viewBox="0 0 44 36" fill="none" stroke="#ffffff" stroke-width="5"><path d="M2 18h38M24 3l16 15-16 15"/></svg>
</div>
<div class="card" style="left:813px">
  <svg class="icon" width="96" height="96" viewBox="0 0 96 96" fill="none" stroke="#1c1c1c" stroke-width="3"><path d="M14 86V12h44l12 12v18"/><path d="M24 80V64M34 80V56M44 80V60"/><circle cx="70" cy="62" r="14"/><circle cx="70" cy="62" r="5"/></svg>
  <h4>SPATIAL DATA SOLUTIONS</h4>
  <ul><li>Spatial Data Cleanup</li><li>GIS Data Model Design/Review</li><li>Integrating With Other Systems</li></ul>
  <svg class="arrow" width="44" height="36" viewBox="0 0 44 36" fill="none" stroke="#1c1c1c" stroke-width="5"><path d="M2 18h38M24 3l16 15-16 15"/></svg>
</div>

<section class="products" role="img" aria-label="Night view of the earth from above the clouds with city lights"></section>
<h2 class="section-title" style="top:2698px;color:var(--white)">Our Products</h2>
<div class="tabs">
  <span class="on">GIS MAPPING<br>SOLUTIONS</span><span class="off">SPATIAL ANALYSIS<br>TOOLS</span><span class="off">DATA MANAGEMENT<br>SYSTEMS</span><span class="off">CUSTOM GIS<br>APPLICATIONS</span><span class="off">CONSULTATION AND<br>TRAINING</span>
</div>
<div class="abs" style="left:59px;top:2906px;width:320px;color:var(--white)">
  <h3 style="font-size:31px;font-weight:400;line-height:30px">GIS MAPPING<br>SOLUTIONS</h3>
  <p style="font-size:12.5px;line-height:14.5px;margin-top:12px">Lorem Ipsum È Un Testo Segnaposto Utilizzato Nel Settore Della Tipografia E Della Stampa</p>
  <p style="font-size:12.5px;line-height:14.5px;margin-top:14px">Lorem Ipsum È Un Testo Segnaposto Utilizzato Nel Settore Della Tipografia E Della Stampa. Lorem Ipsum È Considerato Il Testo Segnaposto Standard Sin Dal Sedicesimo Secolo, Quando Un Anonimo Tipografo Prese Una Cassetta Di Caratteri E Li Assemblò Per Preparare Un Testo Campione. È Sopravvissuto Non Solo A Più Di Cinque Secoli, Ma Anche Al Passaggio Alla Videoimpaginazione, Pervenendoci Sostanzialmente Inalterato.</p>
</div>
<div class="round" style="left:60px;top:3215px"><svg width="32" height="32" viewBox="0 0 32 32" fill="none" stroke="#1c1c1c" stroke-width="2"><path d="M22 16H10M15 11l-5 5 5 5"/></svg></div>
<div class="round" style="left:103px;top:3215px"><svg width="32" height="32" viewBox="0 0 32 32" fill="none" stroke="#1c1c1c" stroke-width="2"><path d="M10 16h12M17 11l5 5-5 5"/></svg></div>

<div class="tile" style="left:420px;top:2904px"><div class="pic" style="background:linear-gradient(135deg,#0f3f8a,#1a57b0 60%,#0c2e66)" role="img" aria-label="Blue thematic map of a coastline with yellow highlighted areas"></div><h5>THEMATIC MAPPING</h5><p>Visualize Data Through Thematic Layers To Highlight Specific Trends.</p></div>
<div class="tile hl" style="left:776px;top:2904px"><div class="pic" style="background:radial-gradient(circle at 30% 30%,#2aa7a0,#0c3a40 70%)" role="img" aria-label="Four teal radar screens on a dark interface"></div><h5>INTERACTIVE WEB MAPS</h5><p>Create Engaging, User-Friendly Maps For Web Applications.</p></div>
<div class="tile" style="left:420px;top:3256px"><div class="pic" style="background:radial-gradient(ellipse at 50% 55%,#d9c13a,#3c9a3a 35%,#1f1f1f 62%)" role="img" aria-label="Colourful three-dimensional terrain model"></div><h5>TERRAIN VISUALIZATION</h5><p>Offer Clients A Three-Dimensional Perspective Of Geographic Data.</p></div>
<div class="tile" style="left:776px;top:3256px"><div class="pic" style="background:linear-gradient(135deg,#0a2a5a,#1e6fc8 55%,#0a1f44)" role="img" aria-label="Hand holding a phone under a glowing blue world map with pins"></div><h5>DATA ANALYSIS</h5><p>Transform Raw Data Into Meaningful Insights With Our Advanced Data Analysis And Services</p></div>

<h2 class="section-title" style="top:3718px">Get In Touch</h2>
<p class="section-sub" style="top:3814px">Talk To Someone On Our Sales Team.</p>
<div class="field" style="top:3862px;height:59px">Name</div>
<div class="field" style="top:3941px;height:59px">Your Email</div>
<div class="field" style="top:4020px;height:151px">Your Message</div>
<div class="btn abs" style="left:518px;top:4238px;width:165px;height:41px">SEND</div>

<footer class="footer">
  <div class="brand abs" style="left:66px;top:38px;font-size:20px"><span class="brand-dot" style="width:52px;height:52px"></span><span>TOVESCA<br>GROUP</span></div>
  <div class="fcol" style="left:66px;top:108px"><h6>CUSTOMER SERVICE</h6>Payment Service<br>Track Order</div>
  <div class="fcol" style="left:372px;top:40px"><h6>QUICK LINKS</h6>Home<br>About Us<br>Services<br>Products<br>Contact Us</div>
  <div class="fcol" style="left:607px;top:36px"><h6 style="margin-left:8px">CONTACT US</h6>1800-555-0147<br>care@tovescamail.com<br>Help &amp; Contact<br>FAQS</div>
  <div class="fcol" style="left:922px;top:36px;width:200px;line-height:21px"><i>Lorem Ipsum È Un Testo Segnaposto Utilizzato Nel Settore Della Tipografia E Della Stampa</i>
    <h6 style="margin-top:12px">Follow Us With</h6>
    <div style="display:flex;gap:12px"><span style="width:13px;height:13px;border-radius:50%;background:var(--white)"></span><span style="width:13px;height:13px;border-radius:50%;background:var(--white)"></span><span style="width:13px;height:13px;border-radius:50%;background:var(--white)"></span><span style="width:13px;height:13px;border-radius:50%;background:var(--white)"></span></div>
  </div>
  <div class="abs" style="left:66px;top:216px;width:1074px;border-top:1px solid #8a8a8a"></div>
  <p class="abs" style="left:0;top:232px;width:1200px;text-align:center;font-size:14px;color:var(--muted)">© 2024 Northvale Limited. All Rights Reserved.&nbsp;&nbsp;&nbsp;&nbsp;&nbsp;&nbsp;Terms &amp; Conditions&nbsp;&nbsp;&nbsp;&nbsp;&nbsp;&nbsp;Privacy Policy</p>
</footer>

</body>
</html>
```